Heavy Equipment Rental Company Looking for Attractive Sign Design

We need a new sign for our forklift rental company in Southern California called Ridgeline Lift Partners. We also sell, service and move forklifts and other equipment, but forklift rentals are our main business. Our old sign on the street is deteriorating quickly. I've attached a photo of the old sign - it is approximately 52" high and 48" wide, but may be made 6" or so taller if needed. The old sign is included more to reference the information than the design - the old design definitely has issues (no SketchHive at the time). The smaller sign reading Borvex dealer is not needed. We want the sign to be simple, clean and easy to read, but of course also attractive and professional. We would like the same information on it as is on the previous sign, but it may be re-arranged. The number 2200 is the street number. Here are the essential elements:
2200 (street number)
Ridgeline Lift Partners (business name)
714-382-0476 (phone)
www.ridgelinelifts-example.com (website)
Forklift Rentals and Sales (main businesses)
If possible, we would like the names of our 2 primary brands:
Borvex and Tavilo Forklifts
Although, if there's no way to implement them nicely, then we can leave them off.

Target Market(s)

Industrial, Construction

Industry/Entity Type

Construction

Colors
0355a3

Requirements
Must have
• Bold, clean, easy to read, with the necessary information.
Nice to have
• Our main machines are all painted blue, so some blue in the design would be nice. In our industry, Borvex forklifts and Tavilo forklifts are two different brands but have good reputations. It would be nice if we can include them in the design, although a nice design is more important than including the brand names.
Should not have
• Small or difficult to read text. Colors or fonts that are too playful.

```html
<!DOCTYPE html>
<html lang="en">
<head>
<meta charset="utf-8">
<title>Ridgeline Lift Partners – Street Sign</title>
<link rel="stylesheet" href="https://fonts.googleapis.com/css2?family=Bebas+Neue&family=Roboto:wght@900&display=swap">
<style>
  :root {
    --sign-blue: #284c9e;
    --sign-face: #f2f2f2;
    --backdrop: #dcdcdc;
    --icon-tint: #c9d3ea;
    --text-light: #f2f2f2;
  }
  html, body {
    margin: 0;
    padding: 0;
    width: 1200px;
    height: 970px;
    overflow: hidden;
    background: var(--backdrop);
  }
  .sign {
    position: absolute;
    left: 296px;
    top: 106px;
    width: 596px;
    height: 744px;
    background: var(--sign-face);
  }
  .sign svg { display: block; }
  .frame-line { fill: none; stroke: var(--sign-blue); stroke-width: 5; stroke-linecap: round; }
  .headline { font-family: "Bebas Neue", sans-serif; fill: var(--sign-blue); }
  .street-number { font-family: "Roboto", Arial, sans-serif; font-weight: 900; fill: var(--text-light); }
  .band-text { font-family: "Bebas Neue", sans-serif; fill: var(--text-light); }
  .fill-blue { fill: var(--sign-blue); }
  .icon-slot { fill: var(--icon-tint); }
</style>
</head>
<body>
  <div class="sign">
    <svg width="596" height="744" viewBox="0 0 596 744" xmlns="http://www.w3.org/2000/svg">
      <!-- top frame -->
      <path class="frame-line" d="M20 122 V64 Q20 54 30 54 H205 M390 54 H564 Q574 54 574 64 V122"/>
      <rect class="fill-blue" x="205" y="20" width="185" height="69" rx="5"/>
      <text class="street-number" x="297.5" y="76" font-size="58" text-anchor="middle">2200</text>

      <!-- business name -->
      <text class="headline" x="302" y="186" font-size="86" text-anchor="middle" textLength="404" lengthAdjust="spacingAndGlyphs">RIDGELINE</text>
      <text class="headline" x="302" y="314" font-size="143" text-anchor="middle" textLength="260" lengthAdjust="spacingAndGlyphs">LIFT</text>

      <!-- forklift icon areas -->
      <rect class="icon-slot" x="12" y="262" width="68" height="76" rx="4" role="img" aria-label="Outline forklift icon facing right"/>
      <rect class="icon-slot" x="514" y="262" width="68" height="76" rx="4" role="img" aria-label="Outline forklift icon facing left"/>

      <path class="frame-line" d="M88 351 H256 M342 351 H504" stroke-width="3"/>

      <text class="headline" x="302" y="418" font-size="80" text-anchor="middle" textLength="404" lengthAdjust="spacing">PARTNERS</text>

      <!-- bottom frame -->
      <path class="frame-line" d="M22 423 V716 Q22 726 32 726 H563 Q573 726 573 716 V423"/>

      <text class="headline" x="298" y="485" font-size="55" text-anchor="middle" textLength="512" lengthAdjust="spacingAndGlyphs">WWW.RIDGELINELIFTS-EXAMPLE.COM</text>

      <rect class="fill-blue" x="22" y="499" width="551" height="59"/>
      <text class="band-text" x="298" y="551" font-size="58" text-anchor="middle" textLength="516" lengthAdjust="spacingAndGlyphs">FORKLIFT RENTALS AND SALES</text>

      <path class="frame-line" d="M22 644 H573"/>
      <text class="headline" x="303" y="628" font-size="78" text-anchor="middle" textLength="406" lengthAdjust="spacing">714-382-0476</text>

      <!-- brands -->
      <text class="headline" x="160" y="701" font-size="48" text-anchor="middle" textLength="200" lengthAdjust="spacing">BORVEX</text>
      <text class="headline" x="424" y="701" font-size="48" text-anchor="middle" textLength="200" lengthAdjust="spacing">TAVILO</text>
    </svg>
  </div>
</body>
</html>
```